Drone company needs a brochure design

We would like a brochure design which compliments our existing logo, website and business card designs.

www.bramblecrest.com.au

```html
<!DOCTYPE html>
<html lang="en">
<head>
<meta charset="utf-8">
<title>Bramblecrest Brochure – Inside Spread</title>
<link rel="stylesheet" href="https://fonts.googleapis.com/css2?family=Exo+2:wght@600;700&family=Ubuntu:wght@300;400&display=swap">
<style>
  :root {
    --backdrop: #ececec;
    --paper: #ffffff;
    --brand-blue: #1e9be0;
    --ink: #1a1a1a;
    --body-grey: #5a5a5a;
    --sea-deep: #0f3f8a;
    --sea-light: #2f78cc;
    --sky: #a9cdee;
    --foliage: #4f7d3a;
    --lawn: #7cb342;
    --fold-shade: rgba(0,0,0,0.08);
  }
  * { margin: 0; padding: 0; box-sizing: border-box; }
  html, body { width: 1200px; height: 900px; overflow: hidden; }
  body {
    background: var(--backdrop);
    font-family: "Ubuntu", sans-serif;
    color: var(--body-grey);
  }
  .spread {
    position: absolute;
    left: 60px; top: 110px;
    width: 1080px; height: 680px;
    background: var(--paper);
    box-shadow: 0 18px 40px rgba(0,0,0,0.15);
  }
  .page { position: absolute; top: 0; width: 540px; height: 680px; }
  .page--left { left: 0; }
  .page--right { left: 540px; }
  .fold {
    position: absolute; left: 534px; top: 0; width: 12px; height: 680px;
    background: linear-gradient(90deg, transparent, var(--fold-shade), transparent);
    z-index: 3;
  }
  .photo-harbour {
    position: absolute; left: 0; top: 0; width: 540px; height: 290px;
    background: linear-gradient(180deg, var(--sky) 0%, var(--sea-light) 45%, var(--sea-deep) 100%);
  }
  .about {
    position: absolute; left: 60px; top: 330px; width: 320px;
  }
  .section-title {
    font-family: "Exo 2", sans-serif; font-weight: 700;
    font-size: 26px; color: var(--ink); line-height: 1;
  }
  .section-title .accent { color: var(--brand-blue); }
  .about__text {
    margin-top: 14px; font-size: 13px; line-height: 1.32; color: var(--body-grey);
  }
  .tagline {
    position: absolute; left: 60px; top: 530px; width: 300px;
    color: var(--brand-blue); font-weight: 300; text-transform: uppercase;
    font-size: 19px; line-height: 1.2; text-align: center;
  }
  .tagline__big { display: block; font-size: 28px; }
  .photo-estate {
    position: absolute; left: 400px; top: 405px; width: 680px; height: 275px;
    background: linear-gradient(180deg, var(--sky) 0%, var(--foliage) 18%, #6a9a45 50%, var(--lawn) 75%, #5f8f3a 100%);
    z-index: 1;
  }
  .services {
    position: absolute; left: 40px; top: 38px; width: 470px;
  }
  .services__grid {
    display: grid; grid-template-columns: repeat(3, 1fr); column-gap: 18px;
    margin-top: 14px;
  }
  .service { margin-bottom: 14px; }
  .service__heading {
    font-size: 8.5px; text-transform: uppercase; color: var(--brand-blue);
    letter-spacing: 0.3px; margin-bottom: 4px;
  }
  .service__text {
    font-size: 9.5px; line-height: 1.3; color: var(--body-grey);
    text-align: justify; hyphens: auto;
  }
</style>
</head>
<body>
  <main class="spread">
    <section class="page page--left">
      <div class="photo-harbour" role="img" aria-label="Aerial photo of a harbour breakwater in deep blue water under a clear sky"></div>
      <div class="about">
        <h2 class="section-title"><span class="accent">About</span> Us</h2>
        <p class="about__text">We provide premium aerial media solutions using the latest Unmanned Aerial Vehicles (UAV) technology. Offering a combination of stunning HD aerial filming and breath-taking aerial photography for a variety of different projects. The Bramblecrest team offer a unique service that is bespoke to your application and desired specification.</p>
      </div>
      <p class="tagline">Let us capture your vision and provide you with that <span class="tagline__big">ultimate vantage!</span></p>
    </section>

    <section class="page page--right">
      <div class="services">
        <h2 class="section-title"><span class="accent">Our</span> Services</h2>
        <div class="services__grid">
          <div class="services__col">
            <article class="service">
              <h3 class="service__heading">Real Estate</h3>
              <p class="service__text">Buyers want to learn about the area surrounding their property as much as they want to learn about the property itself. Bramblecrest can showcase important factors like proximity to the coast, lakes, schools, major transport, CBD and the general feel of an area.</p>
            </article>
            <article class="service">
              <h3 class="service__heading">Inspection &amp; Environment</h3>
              <p class="service__text">We eliminate the need for expensive and time consuming scaffolding, man lifting equipment and helicopter charters. Our cameras can be viewed in real-time from the ground by your qualified technicians and we can take in-flight instructions in order to provide the perfect vantage for their specific needs.</p>
            </article>
          </div>
          <div class="services__col">
            <article class="service">
              <h3 class="service__heading">Construction &amp; Property</h3>
              <p class="service__text">We can help you affordably track the progression of your developments so you can update your clients with stunning aerial photos and HD video. Also providing existing properties such as Golf Courses, Hotel Resorts aerial imagery that showcases their properties.</p>
            </article>
            <article class="service">
              <h3 class="service__heading">Survey &amp; Mapping</h3>
              <p class="service__text">Reliable, timely survey data to enhance productivity or for precise Geo-location. Cost effective alternative to conventional aerial surveys &amp; mapping. We are mobile and can travel to remote mine sights and rural farming operations.</p>
            </article>
          </div>
          <div class="services__col">
            <article class="service">
              <h3 class="service__heading">Media &amp; Advertising</h3>
              <p class="service__text">Aerial video and photography are ideal for websites and almost all promotional publications where you need a new perspective to show your products or services to new clients. Let us help you stand out from the pack.</p>
            </article>
            <article class="service">
              <h3 class="service__heading">Insurance &amp; Risk</h3>
              <p class="service__text">Bramblecrest are pleased to work with local insurance companies to inspect damage caused to land and properties. Assisting assessors and loss adjustors for claims. We also provide risk surveying support for underwriters.</p>
            </article>
          </div>
        </div>
      </div>
    </section>

    <div class="photo-estate" role="img" aria-label="Aerial photo of a hillside estate with buildings, shade sails, lawns and rows of orchard trees surrounded by bushland"></div>
    <div class="fold" aria-hidden="true"></div>
  </main>
</body>
</html>
```